2017 New Year Membership Sale

I require a flyer to be designed for a mail box drop.

We are a 24/7 Gym and will be running a sale in January. No Joining Fee, Flexible membership options.

We are also going to have an open day on Saturday the 21st of January, everyone is welcome. Supplement samples and information. Free health measurements. Free starter PT pack if you join on the day.

We offer a 24/7 DIY gym as well as a comprehensive Personal Training Studio.

I have included the design I used last year.

Target Market(s)

Potential Members of all ages.

Industry/Entity Type

Gym

Requirements
Must have
• Our Address, Phone Number.
• Staffed Hours;
• Mon-Thur: 12pm - 7pm
• Fri-Sat: 8am - 1pm

```html
<!DOCTYPE html>
<html lang="en">
<head>
<meta charset="utf-8">
<title>Kestrel Fitness – January Membership Sale</title>
<link rel="stylesheet" href="https://fonts.googleapis.com/css2?family=Montserrat:wght@500;600;700;800&display=swap">
<style>
  :root {
    --orange: #f26a1b;
    --orange-deep: #e0560c;
    --ink: #141414;
    --charcoal: #2b2b2b;
    --paper: #ffffff;
    --paper-grey: #f1f1f1;
    --stage: #d9dbe0;
  }
  * { box-sizing: border-box; margin: 0; padding: 0; }
  html, body {
    width: 1200px; height: 900px; overflow: hidden;
    background: var(--stage);
    font-family: "Montserrat", Arial, sans-serif;
  }
  .flyer {
    position: absolute; left: 295px; top: 20px;
    width: 610px; height: 860px;
    background: var(--paper);
    overflow: hidden;
    box-shadow: 0 6px 24px rgba(0,0,0,.25);
  }
  .abs { position: absolute; }

  /* brand */
  .brand { right: 14px; top: 10px; text-align: right; color: var(--ink); font-weight: 800; }
  .brand-name { font-size: 25px; letter-spacing: 1px; display: flex; align-items: center; gap: 8px; justify-content: flex-end; }
  .brand-dot { width: 14px; height: 14px; border-radius: 50%; background: var(--ink); }
  .brand-place { font-size: 15px; letter-spacing: 9px; font-weight: 600; margin-top: 10px; margin-right: -9px; }

  /* welcome tag */
  .welcome {
    left: 4px; top: 48px; width: 150px; height: 70px;
    background: var(--orange); color: #fff;
    transform: rotate(-20deg);
    font-weight: 700; font-size: 17px; line-height: 1.2; letter-spacing: 1px;
    padding: 13px 0 0 16px;
  }

  /* orange brush band */
  .band {
    left: 0; top: 225px; width: 610px; height: 195px;
    background: linear-gradient(90deg, var(--orange-deep), var(--orange) 60%, #f4803a);
  }

  /* hero photo */
  .hero-ring {
    left: 92px; top: 50px; width: 450px; height: 450px; border-radius: 50%;
    background: #222;
    clip-path: inset(0 0 26% 0);
  }
  .hero-photo {
    left: 104px; top: 62px; width: 424px; height: 424px; border-radius: 50%;
    background: radial-gradient(circle at 40% 35%, #c8b9a6, #8a7866 45%, #4a423a 80%);
    clip-path: inset(0 0 20% 0);
  }

  /* small interior circles */
  .room {
    border-radius: 50%; border: 7px solid var(--paper);
    box-shadow: 0 2px 6px rgba(0,0,0,.25);
  }
  .room-cardio { left: 5px; top: 162px; width: 150px; height: 150px;
    background: linear-gradient(180deg, #eef0f2 0%, #c9ccd0 45%, #4a4c50 100%); }
  .room-weights { left: 0; top: 332px; width: 182px; height: 182px;
    background: linear-gradient(180deg, #f2f3f5 0%, #e37a3a 30%, #9aa0a6 55%, #3e4044 100%); }

  /* headline */
  .headline {
    left: 210px; top: 405px; width: 380px; height: 150px;
    background: var(--orange);
    transform: rotate(-11deg);
    color: #fff; font-weight: 800; font-size: 44px; line-height: 1.1; letter-spacing: 1px;
    padding: 20px 0 0 18px;
  }
  .open-tag {
    left: 102px; top: 505px; width: 122px; height: 70px;
    background: var(--ink); color: #fff;
    transform: rotate(-11deg);
    font-weight: 800; font-size: 28px; line-height: .95; text-align: center;
    padding-top: 6px;
  }

  /* map */
  .map {
    left: 18px; top: 590px; width: 200px; height: 170px;
    background: linear-gradient(135deg, #e6e6e4, #d2d2cf);
    transform: rotate(-8deg) skewX(-4deg);
    box-shadow: 0 2px 8px rgba(0,0,0,.2);
  }

  /* offers */
  .offers {
    left: 232px; top: 590px; width: 260px;
    transform: rotate(-10deg); transform-origin: left top;
    list-style: none; color: var(--ink); font-weight: 600; font-size: 16px; line-height: 1.2;
  }
  .offers li { position: relative; padding-left: 12px; margin-bottom: 8px; }
  .offers li::before {
    content: ""; position: absolute; left: 0; top: 6px;
    width: 8px; height: 8px; border-radius: 50%; background: var(--orange);
  }
  .offers .lead { font-size: 19px; font-weight: 700; }

  /* open day */
  .open-day {
    left: 450px; top: 598px; width: 152px; height: 152px; border-radius: 50%;
    background: radial-gradient(circle at 40% 35%, #4a4a4a, #222);
    color: #fff; text-align: center; font-weight: 700;
    display: flex; flex-direction: column; justify-content: center;
    font-size: 12px; line-height: 1.35;
  }
  .open-day sup { font-size: 7px; }
  .open-day .month { font-size: 17px; margin-top: 6px; }

  /* footer */
  .footer-rule { left: 0; top: 770px; width: 610px; height: 8px; background: var(--orange); }
  .footer {
    left: 0; top: 778px; width: 610px; height: 82px;
    background: linear-gradient(180deg, #1d1d1d, #0c0c0c);
    color: #fff; display: flex; justify-content: space-between; align-items: center;
    padding: 0 18px;
  }
  .hours-title { color: var(--orange); font-weight: 700; font-size: 19px; }
  .hours-line { font-weight: 600; font-size: 14px; line-height: 1.4; }
  .call { text-align: right; font-weight: 800; }
  .call-label { font-size: 22px; letter-spacing: 1px; }
  .call-number { font-size: 44px; line-height: 1; letter-spacing: 1px; }
</style>
</head>
<body>
<main class="flyer">
  <div class="abs band" role="img" aria-label="Orange paint-brush stroke behind the photo"></div>
  <div class="abs hero-ring"></div>
  <div class="abs hero-photo" role="img" aria-label="Photo of members training with kettlebells"></div>
  <div class="abs room room-cardio" role="img" aria-label="Photo of the cardio area with treadmills"></div>
  <div class="abs room room-weights" role="img" aria-label="Photo of the weights floor"></div>

  <header class="abs brand">
    <div class="brand-name"><span class="brand-dot"></span>KESTREL FITNESS</div>
    <div class="brand-place">ASHBURY</div>
  </header>

  <div class="abs welcome">EVERYONE<br>IS WELCOME.</div>

  <h1 class="abs headline">HUGE SALE<br>IN JANUARY</h1>
  <div class="abs open-tag">24/7<br>OPEN</div>

  <div class="abs map" role="img" aria-label="Street map showing the gym location"></div>

  <ul class="abs offers">
    <li class="lead">NO JOINING FEE</li>
    <li>Flexible<br>Membership Options</li>
    <li>Supplement Samples<br>and Information</li>
    <li>Free Measurements</li>
    <li>Free Starter PT pack</li>
  </ul>

  <div class="abs open-day">
    <span>OPEN DAY</span>
    <span>ON SATURDAY 21<sup>ST</sup></span>
    <span class="month">JANUARY</span>
  </div>

  <div class="abs footer-rule"></div>
  <footer class="abs footer">
    <div class="hours">
      <div class="hours-title">STAFFED HOURS</div>
      <div class="hours-line">Mon-Thur: 12pm - 7pm</div>
      <div class="hours-line">Fri -Sat: 8am - 1pm</div>
    </div>
    <div class="call">
      <div class="call-label">CALL US NOW</div>
      <div class="call-number">39450182</div>
    </div>
  </footer>
</main>
</body>
</html>
```